Hearthside BBQ Co. Rub and Sauce Labels

I am bringing to market 3 different meat rubs and 2 BBQ sauces. These rubs and sauces will be sold on an eCommerce website and also at local events. I am looking for simplicity. I believe the BBQ seasoning labels out there are very busy. I am looking for each label to be similar, yet distinct enough to clearly differentiate the different rubs in my offerings. My logo is attached. The Flaming F in my logo is going to be a feature in my brand and would like to have it be a feature on my labels, too. The rubs will be packaged in a traditional clear plastic shaker with a pop-top. I am open to ideas on packaging options as well. The different rubs in the shakers will range in color from very light to dark brown, depending on the ingredients in each rub. Please include all FDA required information on the labels. The rub labels will go on a clear plastic shaker and the sauce will be packaged in a bottle. Thanks for your help and I look forward to seeing your creativity come to life!

Colors

Designer to choose colors to be used in the design.

Requirements
Must have
• Simplicity, yet ability to separate multiple products by simple changes in logo and/or packaging. Please see the attached photo of a competitors bbq sauce - something simple yet flexible.
Nice to have
• Flexibility in design.

```html
<!DOCTYPE html>
<html lang="en">
<head>
<meta charset="utf-8">
<title>Hearthside BBQ Co. — Sauce Labels</title>
<link href="https://fonts.googleapis.com/css2?family=Alfa+Slab+One&family=Archivo+Black&family=Roboto:wght@400&family=Roboto+Condensed:wght@400&family=Archivo:wght@400&display=swap" rel="stylesheet">
<style>
  :root {
    --page: #ffffff;
    --panel-black: #111111;
    --ink-white: #ffffff;
    --flame-orange: #f2913a;
    --gold-top: #a86a06;
    --gold-bottom: #734502;
    --gold-title: #e8c27a;
    --smoky-top: #7e1b17;
    --smoky-bottom: #4a0d0d;
    --smoky-title: #e39089;
    --carolina-top: #1e2d8e;
    --carolina-bottom: #0f1a5a;
    --carolina-title: #7d9ff2;
  }
  * { margin: 0; padding: 0; box-sizing: border-box; }
  html, body { width: 1200px; height: 1200px; overflow: hidden; background: var(--page); }
  .label-row {
    position: absolute; left: 30px; top: 420px;
    display: flex; gap: 30px;
  }
  .label {
    position: relative; width: 360px; height: 360px;
    display: flex; overflow: hidden;
  }
  .brand-panel {
    width: 134px; background: var(--panel-black);
    padding-top: 16px; display: flex; flex-direction: column; align-items: center;
  }
  .brand-dot { width: 14px; height: 14px; border-radius: 50%; background: var(--flame-orange); margin-bottom: 8px; }
  .brand-name {
    font-family: "Archivo", sans-serif; font-weight: 400; font-size: 10px;
    letter-spacing: 1px; color: var(--ink-white); text-align: center; line-height: 1.25;
  }
  .flavor-panel {
    flex: 1; padding: 22px 0 0 36px; color: var(--ink-white);
    display: flex; flex-direction: column;
  }
  .label--gold .flavor-panel { background: linear-gradient(90deg, var(--gold-top), var(--gold-bottom)); }
  .label--smoky .flavor-panel { background: linear-gradient(90deg, var(--smoky-top), var(--smoky-bottom)); }
  .label--carolina .flavor-panel { background: linear-gradient(90deg, var(--carolina-top), var(--carolina-bottom)); }
  .flavor-name {
    font-family: "Archivo", sans-serif; font-weight: 400; font-size: 34px;
    text-align: center; padding-right: 20px; line-height: 1;
  }
  .label--gold .flavor-name { color: var(--gold-title); }
  .label--smoky .flavor-name { color: var(--smoky-title); }
  .label--carolina .flavor-name { color: var(--carolina-title); }
  .product-bbq {
    font-family: "Alfa Slab One", serif; font-size: 56px; line-height: 1;
    letter-spacing: 2px; margin-top: 8px; margin-left: -8px;
    transform: scaleX(1.18); transform-origin: left;
  }
  .product-sauce {
    font-family: "Archivo Black", sans-serif; font-size: 32px; line-height: 1;
    letter-spacing: 2px; margin-top: 4px; margin-left: 8px;
  }
  .rule { height: 2px; background: var(--ink-white); margin: 14px 0 14px 0; }
  .description {
    font-family: "Roboto", sans-serif; font-size: 12px; line-height: 16px;
    padding-right: 18px;
  }
  .net-weight {
    font-family: "Roboto Condensed", sans-serif; font-size: 13px;
    margin-top: auto; margin-bottom: 22px; text-align: right; padding-right: 20px;
  }
</style>
</head>
<body>
  <main class="label-row">
    <article class="label label--gold">
      <div class="brand-panel">
        <span class="brand-dot"></span>
        <p class="brand-name">HEARTHSIDE<br>BBQ CO.</p>
      </div>
      <div class="flavor-panel">
        <h2 class="flavor-name">GOLD</h2>
        <p class="product-bbq">BBQ</p>
        <p class="product-sauce">SAUCE</p>
        <div class="rule"></div>
        <p class="description">Lorem Ipsum. Proin gravida nibh vel velit auctor aliquet. Aenean sollicitudin, lorem quis bibendum auctor, nisi elit consequat ipsum, nec sagittis sem nibh id elit.</p>
        <p class="net-weight">Net Wt. 20 oz (1.25 lbs.)</p>
      </div>
    </article>
    <article class="label label--smoky">
      <div class="brand-panel">
        <span class="brand-dot"></span>
        <p class="brand-name">HEARTHSIDE<br>BBQ CO.</p>
      </div>
      <div class="flavor-panel">
        <h2 class="flavor-name">SMOKY</h2>
        <p class="product-bbq">BBQ</p>
        <p class="product-sauce">SAUCE</p>
        <div class="rule"></div>
        <p class="description">Lorem Ipsum. Proin gravida nibh vel velit auctor aliquet. Aenean sollicitudin, lorem quis bibendum auctor, nisi elit consequat ipsum, nec sagittis sem nibh id elit.</p>
        <p class="net-weight">Net Wt. 20 oz (1.25 lbs.)</p>
      </div>
    </article>
    <article class="label label--carolina">
      <div class="brand-panel">
        <span class="brand-dot"></span>
        <p class="brand-name">HEARTHSIDE<br>BBQ CO.</p>
      </div>
      <div class="flavor-panel">
        <h2 class="flavor-name">CAROLINA</h2>
        <p class="product-bbq">BBQ</p>
        <p class="product-sauce">SAUCE</p>
        <div class="rule"></div>
        <p class="description">Lorem Ipsum. Proin gravida nibh vel velit auctor aliquet. Aenean sollicitudin, lorem quis bibendum auctor, nisi elit consequat ipsum, nec sagittis sem nibh id elit.</p>
        <p class="net-weight">Net Wt. 20 oz (1.25 lbs.)</p>
      </div>
    </article>
  </main>
</body>
</html>
```